Young Accounting firm needing a captivating business card

We need a business card design that forces the person to look at the card because its either gold foil, plastic, or lettering pop up etc. We already have a logo with a specific gold color and we need to make it pop. We are an accounting firm. I need the words" accounting, payroll, licenses, audits, taxes" somewhere on the business card so as to describe what we do- preferably on the side where the logo is at.

Industry/Entity Type

Accounting

Contact Information for Business Card

Address 48276 9th Ave S Ste 305, Federal Way, WA 98117
Business Phone (360)418-2096
Fax (360)418-2157
Office Cell Phone (360)586-7319

Font styles to use
Serif

Colors
85abd2

Requirements
Must have
• It should state
• "Accounting" "Taxes" "Audits" "Licenses" "Payroll"
Nice to have
• Matte with gold foil, different textures, With Either a textured ivory background or gray blue slate background
Should not have
• colorful colors

```html
<!DOCTYPE html>
<html lang="en">
<head>
<meta charset="utf-8">
<title>Ledgerline Business Card</title>
<link href="https://fonts.googleapis.com/css2?family=Arimo:ital,wght@0,700;1,700&family=Open+Sans:ital,wght@1,500&family=Raleway:wght@400;500&display=swap" rel="stylesheet">
<style>
  :root {
    --backdrop: #6d7a80;
    --card: #ffffff;
    --gold: #b38a10;
    --slate-blue: #85abd2;
    --ink: #555555;
    --ink-dark: #2b2b2b;
    --line: #444444;
  }
  html, body {
    margin: 0;
    width: 1200px;
    height: 1200px;
    overflow: hidden;
    background: var(--backdrop);
  }
  .card {
    position: absolute;
    background: var(--card);
    overflow: hidden;
  }
  .card-front { left: 257px; top: 121px; width: 695px; height: 414px; }
  .card-back  { left: 258px; top: 620px; width: 697px; height: 418px; }

  .brand {
    position: absolute;
    font-family: "Raleway", sans-serif;
    font-weight: 500;
    white-space: nowrap;
    text-align: center;
    line-height: 1.15;
  }
  .brand-mark {
    display: block;
    margin: 0 auto;
  }
  .front-brand { left: 66px; top: 157px; width: 230px; color: var(--gold); font-size: 37px; }
  .front-brand .brand-mark { width: 56px; height: 56px; background: var(--gold); margin-bottom: 6px; }

  .divider { position: absolute; left: 338px; top: 148px; width: 1px; height: 118px; background: var(--line); }

  .contact { position: absolute; left: 411px; top: 99px; font-family: "Raleway", sans-serif; color: var(--ink); }
  .contact-name { font-family: "Arimo", sans-serif; font-weight: 700; color: var(--gold); font-size: 16px; margin: 0; letter-spacing: .3px; }
  .contact-title { font-family: "Arimo", sans-serif; font-weight: 700; color: var(--gold); font-size: 13.5px; margin: 3px 0 6px; }
  .contact-address { font-size: 14px; line-height: 19px; margin: 0; }
  .contact-list { list-style: none; padding: 0; margin: 24px 0 0; font-size: 14.5px; }
  .contact-list li { display: flex; align-items: center; height: 19.5px; }
  .contact-list svg { width: 13px; height: 13px; margin-right: 17px; fill: var(--gold); }

  .services-band {
    position: absolute; left: 22px; top: 335px; width: 651px; height: 42px;
    background: var(--slate-blue);
    display: flex; align-items: center; justify-content: center;
    font-family: "Arimo", sans-serif; font-style: italic; font-weight: 700;
    color: #fff; font-size: 14.4px; letter-spacing: .5px; word-spacing: 8px;
  }

  .back-panel { position: absolute; left: 22px; top: 22px; width: 653px; height: 312px; background: var(--slate-blue); }
  .back-brand { left: 0; top: 122px; width: 697px; color: #fff; font-size: 62px; }
  .back-brand .brand-mark { width: 70px; height: 70px; background: #fff; margin-bottom: 8px; }
  .back-web {
    position: absolute; left: 22px; top: 334px; width: 653px; height: 34px;
    display: flex; align-items: center; justify-content: center;
    font-family: "Open Sans", sans-serif; font-style: italic; font-weight: 500;
    font-size: 15.7px; color: var(--ink-dark);
  }
  .back-foot { position: absolute; left: 22px; top: 368px; width: 653px; height: 29px; background: var(--slate-blue); }
</style>
</head>
<body>
  <section class="card card-front">
    <div class="brand front-brand"><span class="brand-mark"></span>Ledgerline</div>

    <div class="divider"></div>

    <div class="contact">
      <p class="contact-name">YOUR NAME</p>
      <p class="contact-title">Title/designation</p>
      <p class="contact-address">Address 48276 9th Ave S Ste 305,<br>Federal Way, WA 98117</p>
      <ul class="contact-list">
        <li><svg viewBox="0 0 24 24"><path d="M6.6 10.8a15 15 0 0 0 6.6 6.6l2.2-2.2a1 1 0 0 1 1-.25 11.4 11.4 0 0 0 3.6.6 1 1 0 0 1 1 1V20a1 1 0 0 1-1 1A17 17 0 0 1 3 4a1 1 0 0 1 1-1h3.5a1 1 0 0 1 1 1c0 1.25.2 2.45.6 3.6a1 1 0 0 1-.25 1z"/></svg>(360)418-2096 (Business)</li>
        <li><svg viewBox="0 0 24 24"><path d="M6.6 10.8a15 15 0 0 0 6.6 6.6l2.2-2.2a1 1 0 0 1 1-.25 11.4 11.4 0 0 0 3.6.6 1 1 0 0 1 1 1V20a1 1 0 0 1-1 1A17 17 0 0 1 3 4a1 1 0 0 1 1-1h3.5a1 1 0 0 1 1 1c0 1.25.2 2.45.6 3.6a1 1 0 0 1-.25 1z"/></svg>(360)586-7319 (Office)</li>
        <li><svg viewBox="0 0 24 24"><path d="M7 2h9v6H7zM3 9h18v13H3zm4 4v2h3v-2zm5 0v2h3v-2zm-5 4v2h3v-2zm5 0v2h3v-2z"/></svg>(360)418-2157</li>
        <li><svg viewBox="0 0 24 24"><path d="M2 5h20v14H2zm2 2v.5l8 5.5 8-5.5V7l-8 5.5z"/></svg>www.ledgerline@.com</li>
      </ul>
    </div>

    <div class="services-band">"Accounting" "Taxes" "Audits" "Licenses" "Payroll"</div>
  </section>

  <section class="card card-back">
    <div class="back-panel"></div>
    <div class="brand back-brand"><span class="brand-mark"></span>Ledgerline</div>
    <div class="back-web">www.ledgerline@mailpost.com</div>
    <div class="back-foot"></div>
  </section>
</body>
</html>
```